Hooded Rogue - Game Company Site

Looking for a simple and sleek 3 page design for a game company site. Will provide a logo to be included in the design. Even though we specialize in flash games at the moment, we plan on expanding to other platforms and would like a site similar to console developer sites than flash game portals. Example: http://brightquill.example

Required Pages:
1. Home: advertising the latest game, big image, and possibly a news post
2. Games: a portfolio of games, each game will have a large image preview and some text, with a link to the game
3. About Us:
A roster of employees, each will have a picture and bio with name, alias, location, and some text.

Would be nice to have a theme inspired by "villains." The logo should provide the general feel we are looking for. You will find the logo attached as a .PSD (Photoshop) and a .PNG to give a quick preview. Vector .ai and .eps logos have also been attached. Feel free to split the text from the character or make any changes you feel necessary!

About Hooded Rogue
We create flash games and are hoping to expand to iPhone games and other platforms in the future!
Our latest game: http://www.plarvexa.example/games/quentloo/tabrin-quest-2-chapter-1

Target Market(s)

18-30 year old male tech and video game enthusiasts

Industry/Entity Type

Advertising

Requirements
Must have
• Must have the logo that is attached.

```html
<!DOCTYPE html>
<html lang="en">
<head>
<meta charset="utf-8">
<title>Hooded Rogue – Games</title>
<link rel="stylesheet" href="https://fonts.googleapis.com/css2?family=Arimo:wght@400;700&family=Luckiest+Guy&display=swap">
<style>
:root{
  --bg-top:#f2902a;
  --bg-bottom:#fcd22a;
  --panel:#1e1409;
  --panel-edge:#3a2a15;
  --accent:#f7a21f;
  --accent-light:#ffc43a;
  --nav-orange:#f9932a;
  --nav-dark:#17100a;
  --card-top:#3d3d3d;
  --card-bottom:#050505;
  --footer-text:#3b2a12;
}
*{box-sizing:border-box;margin:0;padding:0}
html,body{width:1200px;height:923px;overflow:hidden}
body{
  position:relative;
  font-family:"Arimo",Arial,sans-serif;
  background:linear-gradient(160deg,var(--bg-top) 0%,#f6a52c 45%,var(--bg-bottom) 100%);
}
.sunburst{
  position:absolute;left:0;top:0;width:620px;height:420px;
  background:radial-gradient(ellipse at 45% 25%,rgba(255,214,120,.55) 0%,rgba(255,190,80,.2) 40%,rgba(255,170,60,0) 70%);
}
.brand{
  position:absolute;left:185px;top:26px;width:180px;height:114px;
  display:flex;align-items:center;justify-content:center;gap:8px;
}
.brand-mark{width:18px;height:18px;border-radius:50%;background:var(--nav-dark)}
.brand-name{font-family:"Luckiest Guy",sans-serif;font-size:24px;color:var(--nav-dark);letter-spacing:.5px}

.follow{
  position:absolute;left:818px;top:0;width:225px;height:53px;
  background:var(--panel);border-radius:0 0 4px 4px;
  box-shadow:0 2px 4px rgba(0,0,0,.35);
  display:flex;align-items:center;gap:10px;padding:0 14px;
}
.follow-label{font-family:"Luckiest Guy",sans-serif;font-size:17px;color:var(--accent-light);letter-spacing:.5px}
.social{display:flex;align-items:center;gap:4px;font-size:11px;font-weight:700;color:var(--accent-light)}
.social-square{width:10px;height:10px;background:var(--accent-light);border-radius:2px}

.main-nav a{
  position:absolute;top:99px;height:40px;border-radius:3px;
  font-family:"Luckiest Guy",sans-serif;font-size:18px;letter-spacing:.5px;
  display:flex;align-items:center;justify-content:center;text-decoration:none;
  box-shadow:0 1px 3px rgba(0,0,0,.3);
}
.nav-home{left:642px;width:106px}
.nav-games{left:764px;width:117px}
.nav-about{left:896px;width:148px}
.main-nav .is-idle{background:linear-gradient(#fca43b,var(--nav-orange));color:var(--nav-dark)}
.main-nav .is-current{background:var(--nav-dark);color:var(--accent)}

.games-panel{
  position:absolute;left:153px;top:161px;width:899px;height:661px;
  background:var(--panel);border-radius:8px;
  box-shadow:0 0 4px rgba(0,0,0,.4);
}
.game{position:absolute;width:265px}
.game-title{font-size:26px;font-weight:700;color:var(--accent);height:40px;line-height:40px;margin-left:4px}
.game-preview{
  position:relative;height:149px;margin-top:6px;border:1px solid var(--panel-edge);border-radius:3px;
  background:linear-gradient(var(--card-top),var(--card-bottom));
  display:flex;align-items:center;justify-content:center;
}
.preview-name{font-family:"Luckiest Guy",sans-serif;font-size:20px;color:var(--accent)}
.tag-new{
  position:absolute;left:-11px;top:108px;height:33px;width:74px;
  background:linear-gradient(#ffc43a,var(--accent));
  clip-path:polygon(0 0,88% 0,100% 50%,88% 100%,0 100%);
  font-weight:700;font-size:16px;color:var(--nav-dark);
  padding-left:13px;line-height:33px;
}
.game-blurb{font-size:11.5px;line-height:16px;color:var(--accent);margin:15px 0 0 3px}
.learn-more{
  display:inline-flex;align-items:center;gap:7px;margin:12px 0 0 3px;
  font-size:14px;font-weight:700;color:var(--accent);text-decoration:none;
}
.learn-more svg{width:17px;height:17px}

.site-footer{position:absolute;left:156px;top:846px;width:900px}
.footer-nav a{font-size:14.5px;font-weight:700;color:var(--footer-text);text-decoration:none;margin-right:15px}
.footer-contact{font-size:12px;color:var(--footer-text);margin-top:6px}
.footer-follow{
  position:absolute;left:874px;top:858px;display:flex;align-items:center;gap:10px;
}
.footer-follow .follow-label{color:var(--nav-dark);font-size:16px}
.footer-follow .social{color:var(--nav-dark)}
.footer-follow .social-square{background:var(--nav-dark)}
</style>
</head>
<body>
<div class="sunburst" role="img" aria-label="Soft light rays behind the brand name"></div>

<header>
  <a class="brand" href="#"><span class="brand-mark"></span><span class="brand-name">Hooded Rogue</span></a>
  <div class="follow">
    <span class="follow-label">Follow us:</span>
    <span class="social"><span class="social-square"></span>Friendwall</span>
    <span class="social"><span class="social-square"></span>Chirpline</span>
  </div>
  <nav class="main-nav">
    <a class="nav-home is-idle" href="#">Home</a>
    <a class="nav-games is-current" href="#">Games</a>
    <a class="nav-about is-idle" href="#">About us</a>
  </nav>
</header>

<main class="games-panel">
  <article class="game" style="left:33px;top:26px">
    <h2 class="game-title">Game Title 1</h2>
    <div class="game-preview"><span class="preview-name">Hooded Rogue</span><span class="tag-new">NEW!</span></div>
    <p class="game-blurb">Lorem ipsum dolor sit amet, consectetur adipisicing elit, sed do eiusmod tempor incididunt ut labore et dolore magna aliqua. Ut enim ad minim veniam,</p>
    <a class="learn-more" href="#">LEARN MORE <svg viewBox="0 0 20 20"><circle cx="10" cy="10" r="10" fill="#f7a21f"/><path d="M8 5.5l5.5 4.5L8 14.5z" fill="#1e1409"/></svg></a>
  </article>
  <article class="game" style="left:322px;top:26px">
    <h2 class="game-title">Game Title 2</h2>
    <div class="game-preview"><span class="preview-name">Hooded Rogue</span><span class="tag-new">NEW!</span></div>
    <p class="game-blurb">Lorem ipsum dolor sit amet, consectetur adipisicing elit, sed do eiusmod tempor incididunt ut labore et dolore magna aliqua. Ut enim ad minim veniam,</p>
    <a class="learn-more" href="#">LEARN MORE <svg viewBox="0 0 20 20"><circle cx="10" cy="10" r="10" fill="#f7a21f"/><path d="M8 5.5l5.5 4.5L8 14.5z" fill="#1e1409"/></svg></a>
  </article>
  <article class="game" style="left:610px;top:26px">
    <h2 class="game-title">Game Title 3</h2>
    <div class="game-preview"><span class="preview-name">Hooded Rogue</span></div>
    <p class="game-blurb">Lorem ipsum dolor sit amet, consectetur adipisicing elit, sed do eiusmod tempor incididunt ut labore et dolore magna aliqua. Ut enim ad minim veniam,</p>
    <a class="learn-more" href="#">LEARN MORE <svg viewBox="0 0 20 20"><circle cx="10" cy="10" r="10" fill="#f7a21f"/><path d="M8 5.5l5.5 4.5L8 14.5z" fill="#1e1409"/></svg></a>
  </article>
  <article class="game" style="left:33px;top:339px">
    <h2 class="game-title">Game Title 4</h2>
    <div class="game-preview"><span class="preview-name">Hooded Rogue</span></div>
    <p class="game-blurb">Lorem ipsum dolor sit amet, consectetur adipisicing elit, sed do eiusmod tempor incididunt ut labore et dolore magna aliqua. Ut enim ad minim veniam,</p>
    <a class="learn-more" href="#">LEARN MORE <svg viewBox="0 0 20 20"><circle cx="10" cy="10" r="10" fill="#f7a21f"/><path d="M8 5.5l5.5 4.5L8 14.5z" fill="#1e1409"/></svg></a>
  </article>
  <article class="game" style="left:322px;top:339px">
    <h2 class="game-title">Game Title 5</h2>
    <div class="game-preview"><span class="preview-name">Hooded Rogue</span></div>
    <p class="game-blurb">Lorem ipsum dolor sit amet, consectetur adipisicing elit, sed do eiusmod tempor incididunt ut labore et dolore magna aliqua. Ut enim ad minim veniam,</p>
    <a class="learn-more" href="#">LEARN MORE <svg viewBox="0 0 20 20"><circle cx="10" cy="10" r="10" fill="#f7a21f"/><path d="M8 5.5l5.5 4.5L8 14.5z" fill="#1e1409"/></svg></a>
  </article>
  <article class="game" style="left:610px;top:339px">
    <h2 class="game-title">Game Title 6</h2>
    <div class="game-preview"><span class="preview-name">Hooded Rogue</span></div>
    <p class="game-blurb">Lorem ipsum dolor sit amet, consectetur adipisicing elit, sed do eiusmod tempor incididunt ut labore et dolore magna aliqua. Ut enim ad minim veniam,</p>
    <a class="learn-more" href="#">LEARN MORE <svg viewBox="0 0 20 20"><circle cx="10" cy="10" r="10" fill="#f7a21f"/><path d="M8 5.5l5.5 4.5L8 14.5z" fill="#1e1409"/></svg></a>
  </article>
</main>

<footer>
  <div class="site-footer">
    <nav class="footer-nav"><a href="#">HOME</a> <a href="#">GAMES</a> <a href="#">ABOUT US</a></nav>
    <p class="footer-contact">hello@brightforge.example &nbsp;|&nbsp; Call: 555-018-2740| &nbsp;Fax: 555-018-2740 &nbsp;| © All Rights Reserved</p>
  </div>
  <div class="footer-follow">
    <span class="follow-label">Follow us:</span>
    <span class="social"><span class="social-square"></span>Friendwall</span>
    <span class="social"><span class="social-square"></span>Chirpline</span>
  </div>
</footer>
</body>
</html>
```